TRV Mechanical Solutions Business Card Design

Business card design

Thinking just large logo on one side with a phone number and the back side is contact info with services we offer with a industrial plant across the bottom of the card

See must haves. I will be laser etching these business cards on black metal business cards as well as full color card stock. So must be bold and professional.

Target Market(s)

Industrial manufacturing

Contact Information for Business Card

Industrial manufacturing construction business specializing in consulting project managment and completing projects turn key

Font styles to use
Other font styles liked:
• See Logo for colors and font style

Requirements
Must have
• TRV Mechanical Solutions
• Gerald Munroe
• 2847 Alderwick Lane
• Millbrook, VA, 22947
• Project Managment
• Consulting
• Turn Key Industrial Projects
• I’d like a industrial manufacturing “cityline” on the back side bottom of the
• I’d like to be able to print these business cards in regular color on card stock but I’d also like the design to be etched into black metal business cards

```html
<!DOCTYPE html>
<html lang="en">
<head>
<meta charset="utf-8">
<title>TRV Mechanical Solutions – Business Cards</title>
<link rel="stylesheet" href="https://fonts.googleapis.com/css2?family=Work+Sans:wght@400;500;600&display=swap">
<style>
  :root {
    --backdrop: #262626;
    --backdrop-edge: #161616;
    --card: #1b1b1b;
    --card-light: #252525;
    --silver: #e2e2e2;
    --silver-soft: #bdbdbd;
    --gloss: #3c3c3c;
    --address: #4a4a4a;
    --rule: #8a8a8a;
  }
  * { margin: 0; padding: 0; box-sizing: border-box; }
  html, body { width: 1200px; height: 900px; overflow: hidden; }
  body {
    background: radial-gradient(ellipse at 55% 40%, var(--backdrop), var(--backdrop-edge));
    font-family: "Work Sans", sans-serif;
    position: relative;
  }
  .card {
    position: absolute;
    left: 270px;
    width: 660px;
    height: 377px;
    background: linear-gradient(135deg, var(--card) 0%, var(--card-light) 70%, var(--card) 100%);
    box-shadow: 0 18px 40px rgba(0,0,0,.55);
  }
  .card--front { top: 50px; }
  .card--back { top: 470px; }

  /* Front */
  .front-brand {
    position: absolute;
    top: 120px;
    left: 0; right: 0;
    display: flex;
    justify-content: center;
    align-items: center;
    gap: 16px;
  }
  .brand-square {
    width: 34px; height: 34px;
    background: var(--silver);
    flex: none;
  }
  .front-brand .brand-name {
    font-size: 38px;
    font-weight: 600;
    color: var(--silver);
    letter-spacing: .5px;
  }
  .front-address {
    position: absolute;
    bottom: 58px;
    left: 0; right: 0;
    text-align: center;
    font-size: 16px;
    font-weight: 500;
    color: var(--address);
    letter-spacing: .6px;
  }

  /* Back */
  .back-brand {
    position: absolute;
    top: 112px;
    left: 32px;
    width: 284px;
    display: flex;
    align-items: center;
    gap: 12px;
  }
  .back-brand .brand-square { width: 28px; height: 28px; background: var(--gloss); }
  .back-brand .brand-name {
    font-size: 28px;
    font-weight: 600;
    line-height: 1.15;
    color: var(--gloss);
  }
  .divider {
    position: absolute;
    left: 330px;
    top: 42px;
    width: 1px;
    height: 230px;
    background: var(--rule);
  }
  .details {
    position: absolute;
    left: 362px;
    top: 48px;
    color: var(--silver);
  }
  .person-name {
    font-size: 26px;
    font-weight: 500;
    letter-spacing: 1.2px;
    text-transform: uppercase;
  }
  .person-title {
    font-size: 15px;
    color: var(--silver-soft);
    letter-spacing: .6px;
    margin-bottom: 20px;
  }
  .contact-list { list-style: none; }
  .contact-list li {
    display: flex;
    align-items: center;
    gap: 12px;
    font-size: 17px;
    letter-spacing: .5px;
    line-height: 24px;
  }
  .contact-list svg { width: 13px; height: 13px; flex: none; }
  .services {
    list-style: none;
    margin-top: 20px;
  }
  .services li {
    font-size: 18px;
    letter-spacing: .6px;
    line-height: 25px;
    color: var(--silver);
  }
</style>
</head>
<body>

<section class="card card--front" aria-label="Card front">
  <div class="front-brand">
    <span class="brand-square"></span>
    <span class="brand-name">TRV Mechanical Solutions</span>
  </div>
  <p class="front-address">2847 Alderwick Lane Millbrook, VA, 22947</p>
</section>

<section class="card card--back" aria-label="Card back">
  <div class="back-brand">
    <span class="brand-square"></span>
    <span class="brand-name">TRV Mechanical Solutions</span>
  </div>

  <div class="divider"></div>

  <div class="details">
    <h1 class="person-name">Gerald Munroe</h1>
    <p class="person-title">Director</p>

    <ul class="contact-list">
      <li>
        <svg viewBox="0 0 24 24" fill="currentColor" aria-hidden="true"><path d="M6.6 10.8c1.4 2.8 3.8 5.1 6.6 6.6l2.2-2.2c.3-.3.7-.4 1-.2 1.1.4 2.3.6 3.6.6.6 0 1 .4 1 1V20c0 .6-.4 1-1 1C10.6 21 3 13.4 3 4c0-.6.4-1 1-1h3.5c.6 0 1 .4 1 1 0 1.3.2 2.5.6 3.6.1.3 0 .7-.2 1L6.6 10.8z"/></svg>
        410 5720-3186
      </li>
      <li>
        <svg viewBox="0 0 24 24" fill="none" stroke="currentColor" stroke-width="2" aria-hidden="true"><rect x="3" y="5" width="18" height="14" rx="1"/><path d="M3 6l9 7 9-7"/></svg>
        info@trvmechanical.com
      </li>
      <li>
        <svg viewBox="0 0 24 24" fill="none" stroke="currentColor" stroke-width="2" aria-hidden="true"><circle cx="12" cy="12" r="9"/><path d="M3 12h18M12 3c3 3 3 15 0 18M12 3c-3 3-3 15 0 18"/></svg>
        www.trvmechanical.com
      </li>
    </ul>

    <ul class="services">
      <li>Project Managment</li>
      <li>Consulting</li>
      <li>Turn Key Industrial Projects</li>
    </ul>
  </div>
</section>

</body>
</html>
```